Free Charity Events from KORVAPLAY

The purpose of the landing page is to get all visitors excited about playing in our Free $500 Charity Tournaments. The visitors who click on the landing page will receive 3 free entries into 3 different $500 Charity Tournaments. A $500 Blackjack Tournament, a $500 Texas Holdem Tournament, and a $500 Baccarat Tournament.

We also offer Free Qualifying games 24/7, where players can earn additional entries into our real paying tournaments.

We will reward the winners in each tournament with a share of the $500 and we will reward a worthy cause or charity with $500 as well.

The money comes from advertising shown during the qualifying game.

Our website is currently being developed on our teams development server. Here is a private link to the site. https://dev.korvaplay.example Attached are vector images of our logo.

Also attached are two attempts we made at a landing page.

Target Market(s)

Social Game Players

Industry/Entity Type

Games

Contact Information for Business Card

The purpose of the business card will be to promote our Free Charity Games. There will be a code hand written on the card. (Meaning we will need a white box to write the code in) If the holder of the card enters that code during registration, they will receive 3 free entries into our real cash tournaments. The giver of the card will receive the affiliate bonus for referring a new player.

Font styles to use
Serif
Sans Serif

Colors
9bcb3c
0292cd
ec1f27

Requirements
Must have
• Excitement, i also like humor but that isn't a must, excitement is.
Nice to have
• Humor
Should not have
• Too many words, we are looking for that image that says at least a few hundred words.

```html
<!DOCTYPE html>
<html lang="en">
<head>
<meta charset="utf-8">
<title>KORVAPLAY – Free $500 Charity Tournaments</title>
<link rel="stylesheet" href="https://fonts.googleapis.com/css2?family=Oswald:wght@500;600&family=Poppins:wght@500;600&family=Raleway:wght@400;500;700&display=swap">
<style>
  :root {
    --page-bg: #f4f4f4;
    --white: #ffffff;
    --felt-dark: #0f2212;
    --felt-mid: #1f3d22;
    --felt-red: #3a1414;
    --night: #000000;
    --night-soft: #1a1a1a;
    --brand-green: #9bcb3c;
    --brand-blue: #0292cd;
    --brand-red: #ec1f27;
  }
  * { margin: 0; padding: 0; box-sizing: border-box; }
  html, body {
    width: 1200px;
    height: 2318px;
    overflow: hidden;
    background: var(--page-bg);
  }
  .board { position: relative; width: 1200px; height: 2318px; }

  .landing {
    position: absolute;
    width: 1006px;
    height: 667px;
    overflow: hidden;
    color: var(--white);
    text-align: center;
  }
  .landing--hero { left: 239px; top: 126px; transform: scale(0.7197); transform-origin: top left; }
  .landing--felt { left: 97px; top: 793px; }
  .landing--night { left: 97px; top: 1549px; }

  .landing__backdrop { position: absolute; inset: 0; }
  .landing--hero .landing__backdrop,
  .landing--felt .landing__backdrop {
    background:
      radial-gradient(ellipse 40% 45% at 12% 20%, rgba(120,120,110,.45), transparent 70%),
      radial-gradient(ellipse 45% 40% at 15% 85%, rgba(110,25,25,.75), transparent 75%),
      radial-gradient(ellipse 40% 40% at 55% 80%, rgba(60,60,60,.5), transparent 75%),
      linear-gradient(160deg, var(--felt-mid) 0%, var(--felt-dark) 60%, var(--felt-red) 100%);
  }
  .landing--night .landing__backdrop {
    background:
      radial-gradient(ellipse 30% 35% at 30% 80%, rgba(90,90,90,.45), transparent 75%),
      radial-gradient(ellipse 20% 30% at 45% 45%, rgba(80,20,20,.5), transparent 75%),
      linear-gradient(180deg, var(--night) 0%, var(--night-soft) 100%);
  }

  .brand {
    position: absolute;
    top: 22px; left: 0; right: 0;
    display: flex; justify-content: center; align-items: center; gap: 10px;
  }
  .brand__dot {
    width: 44px; height: 44px; border-radius: 50%;
    border: 4px solid var(--white);
  }
  .brand__name {
    font-family: 'Oswald', sans-serif;
    font-weight: 600;
    font-size: 44px;
    line-height: 1;
    letter-spacing: 1px;
  }

  .headline {
    position: absolute; top: 88px; left: 0; right: 0;
    font-family: 'Oswald', sans-serif;
    font-weight: 500;
    font-size: 41px;
    line-height: 1.2;
  }

  .games {
    position: absolute; top: 151px; left: 0; right: 0;
    display: flex; justify-content: center; gap: 39px;
  }
  .game { width: 176px; }
  .game__art {
    width: 176px; height: 176px; border-radius: 50%;
  }
  .game__art--blackjack {
    background: radial-gradient(circle at 60% 45%, #f2f2f2 0%, #c9c9c9 30%, #3c8b4c 65%, #1c1c1c 100%);
  }
  .game__art--holdem {
    background: radial-gradient(circle at 50% 55%, #ffffff 0%, #f0ece6 40%, var(--brand-red) 78%, #c9a23a 100%);
  }
  .game__art--baccarat {
    background: radial-gradient(circle at 40% 60%, #efe4d4 0%, #d8cbb4 40%, var(--brand-green) 80%, #2f9c3e 100%);
  }
  .game__label {
    margin-top: 14px;
    font-family: 'Poppins', sans-serif;
    font-weight: 600;
    font-size: 19px;
    line-height: 24px;
  }

  .qualify {
    position: absolute; top: 417px; left: 0; right: 0;
    font-family: 'Raleway', sans-serif;
    font-weight: 500;
    font-size: 31px;
    line-height: 31px;
  }
  .qualify strong { font-weight: 700; }
  .qualify__note {
    position: absolute; top: 489px; left: 0; right: 0;
    font-family: 'Raleway', sans-serif;
    font-weight: 500;
    font-size: 15px;
  }
  .reward {
    position: absolute; top: 559px; left: 100px; right: 100px;
    font-family: 'Oswald', sans-serif;
    font-weight: 500;
    font-size: 20px;
    line-height: 26px;
  }
</style>
</head>
<body>
<main class="board">

  <section class="landing landing--hero">
    <div class="landing__backdrop" role="img" aria-label="Photo of poker chips and playing cards on green felt"></div>
    <div class="brand"><span class="brand__dot"></span><span class="brand__name">KORVAPLAY</span></div>
    <h1 class="headline">Free $500 Charity Tournaments</h1>
    <div class="games">
      <div class="game"><div class="game__art game__art--blackjack" role="img" aria-label="Blackjack hand of ace and jack"></div><p class="game__label">Blackjack<br>Tournament</p></div>
      <div class="game"><div class="game__art game__art--holdem" role="img" aria-label="Texas Holdem playing cards"></div><p class="game__label">Texas Holdem<br>Tournament</p></div>
      <div class="game"><div class="game__art game__art--baccarat" role="img" aria-label="Hand holding fanned baccarat cards"></div><p class="game__label">Baccarat<br>Tournament</p></div>
    </div>
    <p class="qualify">We also offer Free Qualifying<br>games <strong>24/7</strong></p>
    <p class="qualify__note">where players can earn additional entries into our real paying tournaments.</p>
    <p class="reward">We will reward the winners in each tournament with a share of the $500 and we will reward a worthy cause or charity with $500 as well.</p>
  </section>

  <section class="landing landing--felt">
    <div class="landing__backdrop" role="img" aria-label="Photo of poker chips and playing cards on green felt"></div>
    <div class="brand"><span class="brand__dot"></span><span class="brand__name">KORVAPLAY</span></div>
    <h1 class="headline">Free $500 Charity Tournaments</h1>
    <div class="games">
      <div class="game"><div class="game__art game__art--blackjack" role="img" aria-label="Blackjack hand of ace and jack"></div><p class="game__label">Blackjack<br>Tournament</p></div>
      <div class="game"><div class="game__art game__art--holdem" role="img" aria-label="Texas Holdem playing cards"></div><p class="game__label">Texas Holdem<br>Tournament</p></div>
      <div class="game"><div class="game__art game__art--baccarat" role="img" aria-label="Hand holding fanned baccarat cards"></div><p class="game__label">Baccarat<br>Tournament</p></div>
    </div>
    <p class="qualify">We also offer Free Qualifying<br>games <strong>24/7</strong></p>
    <p class="qualify__note">where players can earn additional entries into our real paying tournaments.</p>
    <p class="reward">We will reward the winners in each tournament with a share of the $500 and we will reward a worthy cause or charity with $500 as well.</p>
  </section>

  <section class="landing landing--night">
    <div class="landing__backdrop" role="img" aria-label="Photo of chip stacks and aces on a black table"></div>
    <div class="brand"><span class="brand__dot"></span><span class="brand__name">KORVAPLAY</span></div>
    <h1 class="headline">Free $500 Charity Tournaments</h1>
    <div class="games">
      <div class="game"><div class="game__art game__art--blackjack" role="img" aria-label="Blackjack hand of ace and jack"></div><p class="game__label">Blackjack<br>Tournament</p></div>
      <div class="game"><div class="game__art game__art--holdem" role="img" aria-label="Texas Holdem playing cards"></div><p class="game__label">Texas Holdem<br>Tournament</p></div>
      <div class="game"><div class="game__art game__art--baccarat" role="img" aria-label="Hand holding fanned baccarat cards"></div><p class="game__label">Baccarat<br>Tournament</p></div>
    </div>
    <p class="qualify">We also offer Free Qualifying<br>games <strong>24/7</strong></p>
    <p class="qualify__note">where players can earn additional entries into our real paying tournaments.</p>
    <p class="reward">We will reward the winners in each tournament with a share of the $500 and we will reward a worthy cause or charity with $500 as well.</p>
  </section>

</main>
</body>
</html>
```